Hydroponic Farm Needs a Business Card

We need a business card design for a hydroponic farm located on the Gulf Coast called 'Mossbrook Farms'. We grow many forms of lettuce and tomatoes along with other herbs and spices. We currently sell to farmer's markets though will soon be expanding to commercial accounts such as restaurants and grocery stores. The colors should be bright and vibrant to reflect the nature of our produce. The final design should communicate a professional, clean, yet friendly impression and able to be used both with farmer's markets and commercial accounts.

The pictures are an example of our product. The pictures do not have to be incorporated into the business card design.

Please put areas for information such as Names, Phone Number, E-mail address, and additional information.

Farm

```html
<!DOCTYPE html>
<html lang="en">
<head>
<meta charset="utf-8">
<title>Mossbrook Farms – Business Card</title>
<link rel="stylesheet" href="https://fonts.googleapis.com/css2?family=Comfortaa:wght@500&display=swap">
<style>
  :root {
    --card-bg: #ffffff;
    --leaf-green: #45b81b;
    --leaf-light: #a8e060;
    --leaf-deep: #3f9a16;
    --brand-red: #7d0a0a;
  }
  html, body {
    margin: 0;
    padding: 0;
    overflow: hidden;
    background: var(--card-bg);
  }
  .card {
    position: relative;
    width: 1200px;
    height: 702px;
    background: var(--card-bg);
    overflow: hidden;
    font-family: "Comfortaa", sans-serif;
    font-weight: 500;
  }
  .brand {
    position: absolute;
    left: 14px;
    top: 33px;
    width: 495px;
    height: 152px;
    display: flex;
    align-items: center;
    gap: 18px;
  }
  .brand-mark {
    width: 34px;
    height: 34px;
    background: var(--brand-red);
    flex: none;
  }
  .brand-name {
    margin: 0;
    font-size: 54px;
    line-height: 1;
    color: var(--brand-red);
    font-weight: 500;
    white-space: nowrap;
  }
  .details {
    position: absolute;
    left: 0;
    top: 0;
    margin: 0;
    padding: 0;
    list-style: none;
    color: var(--leaf-green);
    font-size: 52px;
    line-height: 1;
  }
  .details li {
    position: absolute;
    white-space: nowrap;
  }
  .details .name      { left: 14px; top: 236px; }
  .details .position  { left: 14px; top: 312px; }
  .details .location  { left: 22px; top: 426px; }
  .details .contact   { left: 22px; top: 502px; }
  .details .email     { left: 22px; top: 578px; }
  .produce {
    position: absolute;
    left: 505px;
    top: 185px;
    width: 695px;
    height: 517px;
  }
</style>
</head>
<body>
<main class="card">
  <header class="brand">
    <span class="brand-mark"></span>
    <h1 class="brand-name">Mossbrook Farms</h1>
  </header>

  <ul class="details">
    <li class="name">Name</li>
    <li class="position">Position</li>
    <li class="location">Location</li>
    <li class="contact">Contact Info</li>
    <li class="email">Email Address</li>
  </ul>

  <svg class="produce" viewBox="0 0 695 517" role="img" aria-label="Photograph of fresh frilly green lettuce leaves">
    <defs>
      <radialGradient id="lettuce-tone" cx="70%" cy="65%" r="75%">
        <stop offset="0%" stop-color="var(--leaf-deep)"/>
        <stop offset="55%" stop-color="var(--leaf-green)"/>
        <stop offset="100%" stop-color="var(--leaf-light)"/>
      </radialGradient>
    </defs>
    <path d="M0 517 C20 440 40 330 120 300 C200 230 250 140 350 120 C430 70 520 60 580 30 C630 5 670 0 695 0 L695 517 Z"
          fill="url(#lettuce-tone)"/>
  </svg>
</main>
</body>
</html>
```